New business Card Design

I'm looking to do a new design for our business cards.

Our Company its called the Garden quarter we are a High end outdoor Design and construction company based out of miami FL

Our Style is elegant, minimalist, Luxury but accessible.

see our Website: www.thegardenquarter-example.com

Attached find our logo as well as some samples the cards that we have for our sister company.

Sample Contact information ( in no particular order):

Marco Ventresca
VP of Sales and Marketing
Marco@thegardenquarter-example.com
555.204.7719
4172 NW 63 AVE Miami Florida, 33199

Designs are Looking Great guys but not quite there yet!

Upload your last few designs between today and Tomorrow. we will be choosing one on Saturday!

Cheers, 

Marco Ventresca
Director Of Marketing 

Hello Guys, 

Sorry we have not made a decision yet.  a lot of cool stuff! just narrowing down our options. 
expect a decision with in a day or 2. 

Marco. 

Target Market(s)

high End Design and construction. Luxurious but accessible

Industry/Entity Type

Construction

Colors

Designer to choose colors to be used in the design.

```html
<!DOCTYPE html>
<html lang="en">
<head>
<meta charset="utf-8">
<title>The Garden Quarter – Business Card</title>
<link rel="stylesheet" href="https://fonts.googleapis.com/css2?family=Poiret+One&display=swap">
<style>
  :root {
    --backdrop: #414a4c;
    --card-white: #ffffff;
    --ink-dark: #1c1f1f;
    --ink-soft: #3b4040;
    --sky-top: #2c8ce0;
    --sky-bottom: #5cb8f6;
    --lawn-top: #7fe604;
    --lawn-bottom: #47b007;
    --name-green: #86e81e;
    --name-blue: #3aa9f2;
    --contact-ink: #1e3d10;
    --brand-dot: #3a9f2e;
    --mark-blue: #1f5fc4;
    --icon-light: #eaffd6;
  }
  * { margin: 0; padding: 0; box-sizing: border-box; }
  html, body { width: 1200px; height: 741px; overflow: hidden; }
  body {
    background: var(--backdrop);
    font-family: "Poiret One", "Century Gothic", sans-serif;
    position: relative;
  }
  .card {
    position: absolute;
    left: 400px;
    width: 408px;
    height: 238px;
    overflow: hidden;
  }
  /* Front */
  .card-front {
    top: 90px;
    background: var(--card-white);
    border-top-left-radius: 30px;
  }
  .brand {
    position: absolute;
    left: 12px;
    top: 80px;
    display: flex;
    align-items: center;
    gap: 14px;
  }
  .brand-dot {
    width: 70px;
    height: 70px;
    border-radius: 50%;
    background: var(--brand-dot);
    flex: none;
  }
  .brand-text { display: flex; flex-direction: column; }
  .brand-name {
    font-size: 24px;
    color: var(--ink-dark);
    letter-spacing: 0.5px;
    text-transform: uppercase;
    line-height: 1;
    font-weight: 400;
  }
  .brand-tagline {
    margin-top: 6px;
    font-size: 11px;
    letter-spacing: 3.2px;
    color: var(--ink-soft);
    text-transform: uppercase;
  }
  /* Back */
  .card-back {
    top: 412px;
    background: linear-gradient(to bottom, var(--lawn-top), var(--lawn-bottom));
    border-top-right-radius: 30px;
  }
  .sky-band {
    position: absolute;
    left: 0; top: 0;
    width: 100%;
    height: 89px;
    background: linear-gradient(to bottom, var(--sky-top), var(--sky-bottom));
  }
  .corner-dot {
    position: absolute;
    right: 4px;
    top: 2px;
    width: 106px;
    height: 106px;
    border-radius: 50%;
    background: var(--mark-blue);
  }
  .person-first, .person-last {
    position: absolute;
    font-size: 35px;
    line-height: 1;
  }
  .person-first { left: 12px; top: 55px; color: var(--name-green); }
  .person-last { left: 112px; top: 92px; color: var(--name-blue); }
  .person-title {
    position: absolute;
    left: 30px;
    top: 125px;
    font-size: 11px;
    color: var(--contact-ink);
  }
  .contact {
    position: absolute;
    right: 30px;
    font-size: 11.5px;
    color: var(--contact-ink);
    text-align: right;
    line-height: 1.25;
  }
  .contact-address { top: 155px; }
  .contact-phone { top: 195px; }
  .contact-email { top: 221px; }
  .contact-icon {
    position: absolute;
    right: 8px;
    width: 14px;
    height: 14px;
  }
  .icon-pin { top: 158px; }
  .icon-phone { top: 196px; }
  .icon-mail { top: 222px; }
</style>
</head>
<body>
  <section class="card card-front" aria-label="Card front">
    <div class="brand">
      <span class="brand-dot"></span>
      <div class="brand-text">
        <span class="brand-name">The Garden Quarter</span>
        <span class="brand-tagline">Innovation in Outdoor Design</span>
      </div>
    </div>
  </section>

  <section class="card card-back" aria-label="Card back">
    <div class="sky-band"></div>
    <span class="corner-dot"></span>
    <span class="person-first">Marco</span>
    <span class="person-last">Ventresca</span>
    <span class="person-title">VP of Sales and Marketing</span>

    <p class="contact contact-address">4172 NW 63 AVE<br>Miami Florida, 33199</p>
    <svg class="contact-icon icon-pin" viewBox="0 0 14 14" aria-hidden="true">
      <path d="M7 1a4 4 0 0 1 4 4c0 3-4 8-4 8S3 8 3 5a4 4 0 0 1 4-4z" fill="var(--icon-light)"/>
      <circle cx="7" cy="5" r="1.5" fill="var(--lawn-bottom)"/>
    </svg>

    <p class="contact contact-phone">555.204.7719</p>
    <svg class="contact-icon icon-phone" viewBox="0 0 14 14" aria-hidden="true">
      <rect x="4" y="1" width="6" height="12" rx="1.2" fill="none" stroke="var(--icon-light)" stroke-width="1.2"/>
      <rect x="5.5" y="3" width="3" height="6" fill="var(--icon-light)"/>
    </svg>

    <p class="contact contact-email">Marco@thegardenquarter-example.com</p>
    <svg class="contact-icon icon-mail" viewBox="0 0 14 14" aria-hidden="true">
      <rect x="1" y="3" width="12" height="8" fill="var(--icon-light)"/>
      <path d="M1 3l6 5 6-5" fill="none" stroke="var(--lawn-bottom)" stroke-width="1"/>
    </svg>
  </section>
</body>
</html>
```